KV HOLDINGS Business Cards

I need business cards for "KV Holdings group LLC" doublesided... logo on the back (also include logo on front)
logo attached to project... i have jpg up..
Company Info:
418 North Palmer Avenue, Suite 7B
Chicago, Illinois 60654
facsimile 312-555-0187 (list fax, address, website on all cards.)
www.kvholdingsgroup.example
Three different people on cards:
Darnell P. Okafor, CPA MST
Principal
ofc 312-555-0142
mobile 312-555-0169
darnellpokafor@kvholdingsgroup.example
Gregor T. Vanhoutte, CPA MST
Principal
gregortvanhoutte@kvholdingsgroup.example
mobile 708-555-0113
ofc 312-555-0142
Tobias M Quarrie
Principal
ofc 312-555-0142
no mobile
tobiasmquarrie@kvholdingsgroup.example
I have multiple projects listed.. see below:
Business cards for amber ledge partners llc
letterhead
envelopes
Business cards for KV Holdings LLC
letterhead
envelopes
Target Market(s)
rich people
Industry/Entity Type
Business

```html
<!DOCTYPE html>
<html lang="en">
<head>
<meta charset="utf-8">
<title>KV Holdings Group LLC – Business Cards</title>
<link href="https://fonts.googleapis.com/css2?family=Arimo:wght@400&display=swap" rel="stylesheet">
<style>
  :root {
    --backdrop: #3b3b3b;
    --card-back: #c4c4c4;
    --card-front: #ffffff;
    --brand-blue: #1a4474;
    --ink-blue: #1f4a7c;
    --white: #ffffff;
  }
  html, body {
    margin: 0;
    padding: 0;
    width: 1200px;
    height: 1000px;
    overflow: hidden;
    background: var(--backdrop);
    font-family: "Arimo", Arial, sans-serif;
  }
  .sheet { position: relative; width: 1200px; height: 1000px; }

  .card { position: absolute; width: 500px; height: 292px; overflow: hidden; }
  .card-back { left: 77px; background: var(--card-back); }
  .card-front { left: 624px; background: var(--card-front); }

  .back-name {
    position: absolute;
    left: 0; right: 0; top: 205px;
    text-align: center;
    font-size: 32px;
    letter-spacing: 1px;
    color: var(--brand-blue);
    text-transform: uppercase;
  }

  .front-name {
    position: absolute;
    right: 24px; top: 96px;
    font-size: 15px;
    letter-spacing: 0.5px;
    color: var(--brand-blue);
    text-transform: uppercase;
  }

  .name-band {
    position: absolute;
    left: 0; width: 304px; height: 40px;
    background: var(--brand-blue);
    color: var(--white);
    box-sizing: border-box;
    padding: 4px 0 0 24px;
  }
  .person { display: block; font-size: 19px; line-height: 22px; }
  .title { display: block; font-size: 12px; line-height: 13px; }

  .contacts {
    position: absolute;
    left: 24px;
    margin: 0; padding: 0; list-style: none;
    font-size: 11px; line-height: 14.4px;
    color: var(--ink-blue);
  }
  .company-address {
    position: absolute;
    left: 24px; top: 250px;
    font-size: 11px; line-height: 13px;
    color: var(--ink-blue);
  }
  .foot-band {
    position: absolute;
    left: 0; right: 0; bottom: 0; height: 13px;
    background: var(--brand-blue);
  }
</style>
</head>
<body>
<main class="sheet">

  <section class="card card-back" style="top:31px">
    <div class="back-name">KV Holdings Group LLC</div>
  </section>
  <section class="card card-front" style="top:31px">
    <div class="front-name">KV Holdings Group LLC</div>
    <div class="name-band" style="top:125px">
      <span class="person">Darnell P. Okafor, CPA MST</span>
      <span class="title">Principal</span>
    </div>
    <ul class="contacts" style="top:173px">
      <li>Office : 312-555-0142</li>
      <li>Direct : 312-555-0128</li>
      <li>Mobile : 312-555-0169</li>
      <li>Facsimile : 312-555-0187</li>
      <li>Email : darnellpokafor@kvholdingsgroup.example</li>
    </ul>
    <div class="company-address">418 North Palmer Avenue, Suite 7B Chicago, Illinois 60654<br>www.kvholdingsgroup.example</div>
    <div class="foot-band"></div>
  </section>

  <section class="card card-back" style="top:352px">
    <div class="back-name">KV Holdings Group LLC</div>
  </section>
  <section class="card card-front" style="top:349px">
    <div class="front-name">KV Holdings Group LLC</div>
    <div class="name-band" style="top:127px">
      <span class="person">Gregor T. Vanhoutte, CPA MST</span>
      <span class="title">Principal</span>
    </div>
    <ul class="contacts" style="top:181px">
      <li>Office : 312-555-0142</li>
      <li>Mobile : 708-555-0113</li>
      <li>Facsimile : 312-555-0187</li>
      <li>Email : gregortvanhoutte@kvholdingsgroup.example</li>
    </ul>
    <div class="company-address">418 North Palmer Avenue, Suite 7B Chicago, Illinois 60654<br>www.kvholdingsgroup.example</div>
    <div class="foot-band"></div>
  </section>

  <section class="card card-back" style="top:672px">
    <div class="back-name">KV Holdings Group LLC</div>
  </section>
  <section class="card card-front" style="top:675px">
    <div class="front-name">KV Holdings Group LLC</div>
    <div class="name-band" style="top:126px">
      <span class="person">Tobias M Quarrie</span>
      <span class="title">Principal</span>
    </div>
    <ul class="contacts" style="top:195px">
      <li>Office : 312-555-0142</li>
      <li>Facsimile : 312-555-0187</li>
      <li>Email : tobiasmquarrie@kvholdingsgroup.example</li>
    </ul>
    <div class="company-address">418 North Palmer Avenue, Suite 7B Chicago, Illinois 60654<br>www.kvholdingsgroup.example</div>
    <div class="foot-band"></div>
  </section>

</main>
</body>
</html>
```